Simple AD for Digital Publication

Total Size 5" x 5", may include boarder or not
Image Provided; crop or use as background
Incorporate Logo and text as provided

Target Market(s)

Sound Contractors / Integrators

Industry/Entity Type

Audio Video Lighting

Requirements
Must have
• Bold Look that reflects our brand. see website: merrowfenlight.com - cohesive text and style

```html
<!DOCTYPE html>
<html lang="en">
<head>
<meta charset="utf-8">
<title>Merrowfen Light Co — Become a Dealer</title>
<link rel="stylesheet" href="https://fonts.googleapis.com/css2?family=Montserrat:wght@700;800&display=swap">
<style>
  :root {
    --brand-red: #b00000;
    --brand-red-light: #c01616;
    --white: #ffffff;
    --ink: #3a3a3a;
    --photo-dark: #2a2622;
    --photo-mid: #5b6b3a;
    --photo-floor: #c9b8a6;
  }
  html, body {
    margin: 0;
    padding: 0;
    width: 1200px;
    height: 1200px;
    overflow: hidden;
    background: var(--brand-red);
  }
  .ad {
    position: relative;
    width: 1200px;
    height: 1200px;
    background: var(--brand-red);
    font-family: "Montserrat", Arial, sans-serif;
    overflow: hidden;
  }
  .ad__backdrop {
    position: absolute;
    inset: 0;
  }
  .ad__headline {
    position: absolute;
    top: 72px;
    left: 0;
    width: 100%;
    margin: 0;
    text-align: center;
    color: var(--white);
    font-weight: 700;
    font-size: 53px;
    line-height: 62px;
    letter-spacing: 1.5px;
    text-transform: uppercase;
    text-shadow: 0 2px 6px rgba(0,0,0,0.25);
  }
  .ad__dots {
    position: absolute;
    top: 508px;
  }
  .ad__dots--left { left: 27px; }
  .ad__dots--right { left: 1000px; }
  .ad__feature {
    position: absolute;
    left: 283px;
    top: 241px;
    width: 630px;
    height: 630px;
  }
  .ad__cta-label {
    position: absolute;
    top: 912px;
    left: 0;
    width: 100%;
    margin: 0;
    text-align: center;
    color: var(--white);
    font-weight: 700;
    font-size: 29px;
  }
  .ad__cta-button {
    position: absolute;
    left: 362px;
    top: 958px;
    width: 462px;
    height: 65px;
    border-radius: 33px;
    background: var(--white);
    color: var(--brand-red);
    font-weight: 700;
    font-size: 38px;
    line-height: 65px;
    text-align: center;
    text-decoration: none;
    letter-spacing: 0.5px;
    box-shadow: 0 3px 8px rgba(0,0,0,0.25);
  }
  .ad__brand {
    position: absolute;
    left: 0;
    top: 1072px;
    width: 711px;
    height: 128px;
  }
  .ad__brand-name {
    position: absolute;
    left: 52px;
    top: 1112px;
    display: flex;
    align-items: center;
    gap: 16px;
    color: var(--ink);
    font-weight: 800;
    font-size: 38px;
    letter-spacing: 0.5px;
    text-transform: uppercase;
  }
  .ad__brand-mark {
    width: 44px;
    height: 44px;
    background: var(--brand-red);
  }
</style>
</head>
<body>
  <main class="ad">
    <svg class="ad__backdrop" width="1200" height="1200" viewBox="0 0 1200 1200" aria-hidden="true">
      <polygon points="370,0 830,0 600,55" fill="var(--brand-red-light)" opacity="0.6"/>
      <polygon points="0,1072 606,1072 711,1200 0,1200" fill="var(--white)"/>
    </svg>

    <h1 class="ad__headline">Protect and conceal high<br>and low voltage connectivity</h1>

    <svg class="ad__dots ad__dots--left" width="180" height="96" viewBox="0 0 180 96" aria-hidden="true">
      <g fill="var(--white)">
        <circle cx="6" cy="6" r="3"/><circle cx="48" cy="6" r="3"/><circle cx="90" cy="6" r="3"/><circle cx="132" cy="6" r="3"/><circle cx="174" cy="6" r="3"/>
        <circle cx="6" cy="34" r="3"/><circle cx="48" cy="34" r="3"/><circle cx="90" cy="34" r="3"/><circle cx="132" cy="34" r="3"/><circle cx="174" cy="34" r="3"/>
        <circle cx="6" cy="62" r="3"/><circle cx="48" cy="62" r="3"/><circle cx="90" cy="62" r="3"/><circle cx="132" cy="62" r="3"/><circle cx="174" cy="62" r="3"/>
        <circle cx="6" cy="90" r="3"/><circle cx="48" cy="90" r="3"/><circle cx="90" cy="90" r="3"/><circle cx="132" cy="90" r="3"/><circle cx="174" cy="90" r="3"/>
      </g>
    </svg>
    <svg class="ad__dots ad__dots--right" width="180" height="96" viewBox="0 0 180 96" aria-hidden="true">
      <g fill="var(--white)">
        <circle cx="6" cy="6" r="3"/><circle cx="48" cy="6" r="3"/><circle cx="90" cy="6" r="3"/><circle cx="132" cy="6" r="3"/><circle cx="174" cy="6" r="3"/>
        <circle cx="6" cy="34" r="3"/><circle cx="48" cy="34" r="3"/><circle cx="90" cy="34" r="3"/><circle cx="132" cy="34" r="3"/><circle cx="174" cy="34" r="3"/>
        <circle cx="6" cy="62" r="3"/><circle cx="48" cy="62" r="3"/><circle cx="90" cy="62" r="3"/><circle cx="132" cy="62" r="3"/><circle cx="174" cy="62" r="3"/>
        <circle cx="6" cy="90" r="3"/><circle cx="48" cy="90" r="3"/><circle cx="90" cy="90" r="3"/><circle cx="132" cy="90" r="3"/><circle cx="174" cy="90" r="3"/>
      </g>
    </svg>

    <svg class="ad__feature" width="630" height="630" viewBox="0 0 630 630" role="img" aria-label="Photo of a black stage floor pocket set into a wooden floor, cables running out, with a lit garland of string lights behind it">
      <defs>
        <linearGradient id="feature-fill" x1="0" y1="0" x2="0" y2="1">
          <stop offset="0" stop-color="var(--photo-mid)"/>
          <stop offset="0.42" stop-color="var(--photo-dark)"/>
          <stop offset="0.75" stop-color="#3b342e"/>
          <stop offset="1" stop-color="var(--photo-floor)"/>
        </linearGradient>
      </defs>
      <g transform="rotate(45 315 315)">
        <rect x="91" y="91" width="448" height="448" rx="48" fill="var(--white)"/>
        <rect x="101" y="101" width="428" height="428" rx="40" fill="url(#feature-fill)" transform="rotate(-45 315 315) rotate(45 315 315)"/>
      </g>
    </svg>

    <p class="ad__cta-label">Become a Dealer</p>
    <a class="ad__cta-button" href="https://merrowfenlight.com">CLICK HERE</a>

    <div class="ad__brand-name">
      <span class="ad__brand-mark" aria-hidden="true"></span>
      <span>Merrowfen Light Co</span>
    </div>
  </main>
</body>
</html>
```